Corvell Electrical Flyer

I would like to create a flyer that I can distribute to domestic households outlining the benefits of installing LED down lights in comparison to the older halogen down lights which use more power to run, therefore costing the customer more money.
My aim is to portray the fact that by getting me to install these new LED lights im SAVING the customer money.
I would nee an 'eye catching' headline that will hopefully save my flyer from being thrown out. something along the lines of " SAVE UP TOO $500 A YEAR ON YOUR ELECTRICAL BILL "
The flyer will need to be modern and professional with colour but not too "in your face".
Ive attached some ideas and images that could be used, also two tables that compare the running and replacement cost of the two lights which would be beneficial for the flyer.
I have also attached my company logo which should also be put on the flyer. Thank you
Target Market(s)
Domestic housholds
Industry/Entity Type
Electrical
Look and feel

```html
<!DOCTYPE html>
<html lang="en">
<head>
<meta charset="utf-8">
<title>Corvell Electrical – LED Downlights Flyer</title>
<link rel="stylesheet" href="https://fonts.googleapis.com/css2?family=Roboto+Condensed:wght@400;700&display=swap">
<style>
  :root {
    --page: #ffffff;
    --night: #0c0c0d;
    --night-glow: #3a3a3c;
    --cyan: #2fc4f4;
    --cyan-deep: #12b2ea;
    --cyan-soft: #86dcf7;
    --white: #ffffff;
    --red: #e2290f;
    --red-dark: #8f1a0c;
    --cream: #fff8d6;
    --yellow: #fde38a;
    --ink: #111111;
    --navy: #16384a;
    --brand-grey: #3b4147;
  }
  * { margin: 0; padding: 0; box-sizing: border-box; }
  html, body {
    width: 878px; height: 1200px; overflow: hidden;
    background: var(--page);
    font-family: "Roboto Condensed", "Arial Narrow", sans-serif;
  }
  .flyer {
    position: absolute; left: 40px; top: 33px;
    width: 792px; height: 1122px; overflow: hidden;
  }
  .headline-panel {
    position: absolute; left: 0; top: 0; width: 792px; height: 515px;
    background: radial-gradient(ellipse 60% 55% at 50% 52%, var(--night-glow) 0%, #1c1c1e 45%, var(--night) 100%);
    text-align: center;
  }
  .headline-kicker, .headline-tail {
    position: absolute; left: 0; width: 100%;
    color: var(--cyan); font-weight: 700;
    text-shadow: 0 0 10px rgba(47,196,244,.6);
  }
  .headline-kicker { top: 128px; font-size: 64px; letter-spacing: 1px; }
  .headline-tail {
    top: 358px; font-size: 54px; letter-spacing: 1px;
    transform: scaleX(0.88);
  }
  .headline-amount {
    position: absolute; left: 0; width: 100%; top: 182px;
    color: #f2f4f6; font-weight: 700; font-size: 200px; line-height: 1;
    letter-spacing: 2px;
    transform: scaleX(0.82);
    text-shadow: 0 0 18px rgba(255,255,255,.75), 0 0 40px rgba(200,225,255,.4);
  }
  .basis-band {
    position: absolute; left: 0; top: 515px; width: 792px; height: 67px;
    background: linear-gradient(90deg, var(--red-dark) 0%, var(--red) 45%, var(--red) 60%, var(--red-dark) 100%);
    color: var(--white); font-weight: 700; font-size: 28px;
    display: flex; align-items: center; justify-content: center;
    text-shadow: 0 1px 2px rgba(0,0,0,.4);
  }
  .benefit-panel {
    position: absolute; left: 0; top: 582px; width: 792px; height: 400px;
    background: radial-gradient(ellipse 55% 70% at 50% 60%, var(--cream) 0%, #fff1b8 50%, var(--yellow) 100%);
  }
  .globe-glow {
    position: absolute; left: 170px; top: 20px; width: 450px; height: 380px;
    border-radius: 50%;
    background: radial-gradient(circle, rgba(255,255,255,.9) 0%, rgba(255,255,255,.35) 50%, rgba(255,255,255,0) 72%);
  }
  .question {
    position: absolute; top: 57px;
    color: var(--ink); font-weight: 700; font-size: 24px; line-height: 32px;
  }
  .question--left { left: 66px; text-align: left; }
  .question--middle { left: 300px; width: 230px; text-align: center; }
  .question--right { right: 22px; text-align: right; }
  .call-to-action {
    position: absolute; left: 0; top: 792px; width: 792px;
    text-align: center; color: var(--navy); font-weight: 700;
    font-size: 64px; line-height: 58px;
  }
  .footer-wave { position: absolute; left: 0; top: 0; width: 792px; height: 1122px; }
  .contact-line {
    position: absolute; left: 58px; top: 1036px;
    color: var(--white); font-weight: 700; font-size: 27px;
  }
  .contact-phone {
    position: absolute; left: 371px; top: 1077px;
    color: var(--white); font-weight: 700; font-size: 21px; letter-spacing: .5px;
  }
  .brand {
    position: absolute; right: 12px; top: 1072px;
    display: flex; align-items: center; gap: 8px;
    color: var(--brand-grey); font-weight: 700; font-size: 17px; letter-spacing: 1px;
  }
  .brand-dot {
    width: 20px; height: 20px; border-radius: 50%;
    background: var(--brand-grey);
  }
</style>
</head>
<body>
  <main class="flyer">
    <section class="headline-panel">
      <p class="headline-kicker">SAVE UP TO</p>
      <p class="headline-amount">$500 OFF</p>
      <p class="headline-tail">YOUR ELECTRICITY BILL</p>
    </section>

    <p class="basis-band">Based on changing 20 of your halogen down lights to LED.</p>

    <section class="benefit-panel">
      <div class="globe-glow" role="img" aria-label="Soft glowing LED downlight globe"></div>
      <p class="question question--left">Are you spending<br>too much money on<br>your electrical bill?</p>
      <p class="question question--middle">Sick and tired<br>of changing globes?</p>
      <p class="question question--right">Want to save<br>money while adding<br>value to your house?</p>
    </section>

    <svg class="footer-wave" viewBox="0 0 792 1122" aria-hidden="true">
      <path d="M0 867 C150 925 300 962 420 957 C560 950 700 922 792 898 V1122 H0 Z" fill="var(--cyan-deep)"/>
      <path d="M510 1122 C600 1030 700 965 792 912 V945 C715 992 640 1050 585 1122 Z" fill="var(--cyan-soft)"/>
      <path d="M585 1122 C640 1050 715 992 792 945 V1122 Z" fill="var(--white)"/>
    </svg>

    <h1 class="call-to-action">Install new<br>LED downlights</h1>

    <p class="contact-line">Contact me for an obligation free quote</p>
    <p class="contact-phone">0400731582</p>

    <div class="brand">
      <span class="brand-dot"></span>
      <span>CORVELL ELECTRICAL</span>
    </div>
  </main>
</body>
</html>
```